Design a modern, classy & professional business card for an online real estate agency, specializing in medium-luxury properties in Thailand and later in Singapore and UK.

Possible design ideas so far: (not essential)

- curved corner(s) to the card, white on front & turquoise on back or visa versa.

- front of card - clear and simple, company name in metallic grey/monochrome, logo graphic & company name on front in spot UV or embossed/debossed effect.

- back of card - large, close-cropped, 'ghost' patterns of the C-shaped curves of logo, or company name repeated on back of card in spot UV.

Target Market(s)

- young to middle-aged professionals mainly (but ideally should design should suit all)

- UK, US,EU,AUS & ASIAN mainly (but ideally should design should suit all countries)

Industry/Entity Type

Real Estate

Requirements
Must have
• THEME:
- Luxurious & Modern
- Clean & striking
- Unique & creative

INFO:
- Logo & company name on front
- Contact details on back:

Tobias Lindqvar
Managing Director

www.velmoraestates.example
www.velmoraestates-uk.example

Tel: 084-273-6190
email: tobias@velmoraestates.example

(contact details can be displayed in any order as suites design.)

Nice to have
• - curved corner(s) to the card, white on front & turquoise on back or visa versa.

Should not have
• - No generic images of properties, palm trees/coconut trees etc.

- No other other bold colors, except for main turquoise, grey, metallic white & black theme.

- No obvious business card templates

```html
<!DOCTYPE html>
<html lang="en">
<head>
<meta charset="utf-8">
<title>Velmora Estates – Business Card</title>
<link href="https://fonts.googleapis.com/css2?family=Montserrat:wght@400;500;600;700&display=swap" rel="stylesheet">
<style>
  :root {
    --page-bg: #ffffff;
    --card-white: #ffffff;
    --card-outline: #9a9a9a;
    --brand-grey: #c4c5c7;
    --label-grey: #8c8c8c;
    --turquoise: #37bcbc;
    --text-light: #ffffff;
  }
  * { margin: 0; padding: 0; box-sizing: border-box; }
  html, body {
    width: 1200px;
    height: 1000px;
    overflow: hidden;
    background: var(--page-bg);
    font-family: "Montserrat", sans-serif;
  }
  .sheet {
    position: relative;
    width: 1200px;
    height: 1000px;
  }
  .card {
    position: absolute;
    left: 322px;
    width: 563px;
    height: 368px;
    border-radius: 50px;
  }
  .card--front {
    top: 82px;
    background: var(--card-white);
    border: 1px solid var(--card-outline);
  }
  .card--back {
    top: 532px;
    background: var(--turquoise);
    color: var(--text-light);
  }
  .side-label {
    position: absolute;
    left: 322px;
    width: 563px;
    text-align: center;
    font-weight: 700;
    font-size: 16px;
    letter-spacing: 3px;
    color: var(--label-grey);
  }
  .side-label--front { top: 475px; }
  .side-label--back { top: 925px; }

  /* Front brand lockup */
  .brand {
    position: absolute;
    left: 120px;
    top: 138px;
    display: flex;
    align-items: center;
    gap: 12px;
  }
  .brand__square {
    width: 90px;
    height: 90px;
    background: var(--brand-grey);
    flex-shrink: 0;
  }
  .brand__name {
    font-weight: 500;
    color: var(--brand-grey);
    line-height: 1;
  }
  .brand__name-main {
    display: block;
    font-size: 44px;
    letter-spacing: 0.5px;
  }
  .brand__name-sub {
    display: block;
    margin-top: 10px;
    font-size: 17px;
    letter-spacing: 6.5px;
  }

  /* Back contact block */
  .contact {
    position: absolute;
    right: 32px;
    top: 166px;
    text-align: right;
  }
  .contact__name {
    font-weight: 700;
    font-size: 17px;
    letter-spacing: 2.8px;
    text-transform: uppercase;
  }
  .contact__role {
    margin-top: 6px;
    font-weight: 400;
    font-size: 13.5px;
    letter-spacing: 2.2px;
    text-transform: uppercase;
  }
  .contact__details {
    margin-top: 52px;
    font-size: 13.5px;
    line-height: 19px;
  }
  .contact__line { display: block; font-weight: 400; }
  .contact__line--web { font-weight: 600; }
</style>
</head>
<body>
  <main class="sheet">
    <section class="card card--front" aria-label="Card front">
      <div class="brand">
        <div class="brand__square"></div>
        <div class="brand__name">
          <span class="brand__name-main">Velmora</span>
          <span class="brand__name-sub">ESTATES</span>
        </div>
      </div>
    </section>
    <p class="side-label side-label--front">FRONT</p>

    <section class="card card--back" aria-label="Card back">
      <div class="contact">
        <p class="contact__name">Tobias Lindqvar</p>
        <p class="contact__role">Managing Director</p>
        <p class="contact__details">
          <span class="contact__line">T.084-273-6190</span>
          <span class="contact__line">tobias@velmoraestates.example</span>
          <span class="contact__line contact__line--web">www.velmoraestates.example</span>
          <span class="contact__line contact__line--web">www.velmoraestates-uk.example</span>
        </p>
      </div>
    </section>
    <p class="side-label side-label--back">BACK</p>
  </main>
</body>
</html>
```